Plumber needs a business card

I need a new business card for my plumbing business. I dont have a logo at the moment but I want business cards that are simple but very professional. I want to look like
Name: Mitch Dorley
Address: (just make one up)
Phone: 0455 318 726
Email: mitch@dorleymail.com
Colors to use:
Blacks, blues, silvers

```html
<!DOCTYPE html>
<html lang="en">
<head>
<meta charset="utf-8">
<title>Mitch Dorley – Business Card</title>
<link rel="stylesheet" href="https://fonts.googleapis.com/css2?family=Marcellus+SC&family=Questrial&display=swap">
<style>
  :root {
    --backdrop: #a7b7c1;
    --card-black: #000000;
    --deep-blue: #0a4e78;
    --mid-blue: #0b6fa3;
    --bright-blue: #05b3e8;
    --ice-blue: #a9def3;
    --icon-ink: #0d2636;
    --silver-light: #f2f5f8;
    --silver-dark: #7d8a99;
    --name-white: #ffffff;
  }
  * { margin: 0; padding: 0; box-sizing: border-box; }
  html, body {
    width: 1200px;
    height: 986px;
    overflow: hidden;
    background: var(--backdrop);
  }
  .business-card {
    position: absolute;
    left: 100px;
    top: 207px;
    width: 1000px;
    height: 572px;
    background: var(--card-black);
    overflow: hidden;
  }
  .card-art {
    position: absolute;
    inset: 0;
    width: 100%;
    height: 100%;
  }
  .identity {
    position: absolute;
    left: 113px;
    top: 236px;
    color: var(--name-white);
  }
  .identity__name {
    font-family: "Marcellus SC", serif;
    font-size: 40px;
    font-weight: 400;
    line-height: 1;
    letter-spacing: 1px;
  }
  .identity__role {
    font-family: "Marcellus SC", serif;
    font-size: 22px;
    letter-spacing: 4.5px;
    line-height: 1;
    margin-top: 6px;
  }
  .contact-block {
    position: absolute;
    left: 574px;
    display: flex;
    align-items: flex-start;
    gap: 18px;
    color: var(--ice-blue);
    font-family: "Questrial", sans-serif;
    font-size: 25px;
    line-height: 27px;
  }
  .contact-block--address { top: 182px; }
  .contact-block--reach { top: 320px; }
  .contact-address { font-style: normal; }
  .contact-icon {
    flex: none;
    width: 36px;
    height: 36px;
    margin-top: -2px;
  }
</style>
</head>
<body>
  <article class="business-card">
    <svg class="card-art" viewBox="0 0 1000 572">
      <defs>
        <linearGradient id="lensFill" x1="0" y1="0" x2="1" y2="0">
          <stop offset="0" stop-color="var(--deep-blue)"/>
          <stop offset="0.55" stop-color="var(--mid-blue)"/>
          <stop offset="1" stop-color="var(--bright-blue)"/>
        </linearGradient>
        <radialGradient id="lensGlow" cx="0.95" cy="0.5" r="0.55">
          <stop offset="0" stop-color="#19c4f5" stop-opacity="0.75"/>
          <stop offset="1" stop-color="#19c4f5" stop-opacity="0"/>
        </radialGradient>
        <linearGradient id="silverRim" x1="0" y1="0" x2="0" y2="1">
          <stop offset="0" stop-color="var(--silver-dark)"/>
          <stop offset="0.45" stop-color="var(--silver-light)"/>
          <stop offset="1" stop-color="var(--silver-dark)"/>
        </linearGradient>
      </defs>
      <g class="pipe-pattern-panel" role="img" aria-label="Interlocking plumbing pipe pattern in layered teal blues">
        <path d="M0 0 H322 Q666 286 338 572 H0 Z" fill="url(#lensFill)"/>
        <path d="M0 0 H322 Q666 286 338 572 H0 Z" fill="url(#lensGlow)"/>
      </g>
      <path class="silver-rim" d="M322 0 Q666 286 338 572" fill="none" stroke="url(#silverRim)" stroke-width="4"/>
    </svg>

    <div class="identity">
      <h1 class="identity__name">Mitch Dorley</h1>
      <p class="identity__role">Designation</p>
    </div>

    <div class="contact-block contact-block--address">
      <svg class="contact-icon" viewBox="0 0 36 36" aria-hidden="true">
        <circle cx="18" cy="18" r="17" fill="var(--ice-blue)"/>
        <path d="M18 9 L27 17 H24.5 V26 H20.5 V21 H15.5 V26 H11.5 V17 H9 Z" fill="var(--icon-ink)"/>
      </svg>
      <address class="contact-address">87/14<br>Harbour Road<br>Brookvale - 21045<br>Australia</address>
    </div>

    <div class="contact-block contact-block--reach">
      <svg class="contact-icon" viewBox="0 0 36 36" aria-hidden="true">
        <circle cx="18" cy="18" r="17" fill="var(--ice-blue)"/>
        <path d="M12.5 9.5 L15.5 9 L17.5 13.5 L15.5 15.3 Q17 19.5 20.7 20.5 L22.5 18.5 L27 20.5 L26.5 23.5 Q24.5 26.5 20.5 25.5 Q12.5 23 10.5 15 Q10 11 12.5 9.5 Z" fill="var(--icon-ink)"/>
      </svg>
      <p class="contact-lines">Phone: 0455 318 726<br>Email: mitch@dorleymail.com</p>
    </div>
  </article>
</body>
</html>
```